Custom Truck shop New Business Card design

double sided business card including my new logo, brand colors and picking a font I attached, clean and modern look. I attached the old card for some reference. and would like to include the picture of the white truck attached. I would also like to have it with one of my employees info as well. (same info except name and title Brin Tolvay Service Writer)

Dale Porvick
Owner

address
48310 E Calloway Ridge Rd S
STE 217
Marsh Hollow, CO 80219

phone 720-555-0184

email dale@brokenspurrigs.example

website brokenspurrgis.example

social @brokenspurrigs

Target Market(s)

men 18-60

Industry/Entity Type

Automotive

Contact Information for Business Card

Dale Porvick Owner address 48310 E Calloway Ridge Rd S STE 217 Marsh Hollow, CO 80219 phone 720-555-0184 email dale@brokenspurrigs.example website brokenspurrgis.example social @brokenspurrigs

Font styles to use
Other font styles liked:
• fonts attached

Requirements
Must have
• new logo, orange #FC68D, Charcoal #333333
Nice to have
• the white truck

```html
<!DOCTYPE html>
<html lang="en">
<head>
<meta charset="utf-8">
<title>Broken Spur Rigs – Business Card</title>
<link rel="stylesheet" href="https://fonts.googleapis.com/css2?family=Jost:wght@400;500;700&display=swap">
<style>
  :root {
    --orange: #f26a2a;
    --charcoal: #333333;
    --paper: #ffffff;
    --backdrop: #d9d8d4;
  }
  * { box-sizing: border-box; margin: 0; padding: 0; }
  html, body { width: 1200px; height: 801px; overflow: hidden; }
  body {
    background: var(--backdrop);
    font-family: "Jost", sans-serif;
    color: var(--charcoal);
    display: flex;
    align-items: center;
    justify-content: center;
    gap: 48px;
  }
  .card {
    position: relative;
    width: 540px;
    height: 310px;
    background: var(--paper);
    border-radius: 18px;
    box-shadow: 0 3px 0 var(--orange), 0 14px 30px rgba(0,0,0,0.18);
    overflow: hidden;
  }

  /* brand lockup */
  .brand {
    position: absolute;
    display: flex;
    flex-direction: column;
    align-items: center;
  }
  .brand-dot {
    border-radius: 50%;
    background: var(--charcoal);
  }
  .brand-name {
    font-weight: 700;
    color: var(--charcoal);
    letter-spacing: 0.04em;
    text-transform: uppercase;
    white-space: nowrap;
  }
  .brand-rule {
    height: 2px;
    background: var(--orange);
  }

  /* front */
  .card--front .brand { left: 24px; top: 92px; width: 216px; }
  .card--front .brand-dot { width: 78px; height: 78px; margin-bottom: 14px; }
  .card--front .brand-name { font-size: 18px; }
  .card--front .brand-rule { width: 200px; margin-top: 8px; }

  .divider {
    position: absolute;
    left: 290px; top: 40px;
    width: 2px; height: 230px;
    background: var(--orange);
    transform: rotate(12deg);
  }
  .contact {
    position: absolute;
    left: 322px; top: 52px;
    font-size: 12.5px;
    line-height: 1.4;
  }
  .contact-name { font-size: 22px; font-weight: 700; color: var(--orange); line-height: 1.1; }
  .contact-title { font-size: 13px; margin-bottom: 12px; }
  .contact-address { margin-bottom: 12px; }
  .contact-line { display: flex; align-items: center; gap: 6px; white-space: nowrap; }
  .contact-line svg { width: 11px; height: 11px; flex: none; fill: var(--orange); }

  /* back */
  .card--back .brand { left: 0; right: 0; top: 52px; }
  .card--back .brand-dot { width: 104px; height: 104px; margin-bottom: 18px; }
  .card--back .brand-name { font-size: 36px; }
  .card--back .brand-rule { width: 360px; margin-top: 10px; }
  .social {
    position: absolute;
    right: 34px; bottom: 36px;
    display: flex; align-items: center; gap: 5px;
    font-size: 15px;
  }
  .social-dot { width: 17px; height: 17px; border-radius: 50%; background: var(--orange); }
  .social-handle { margin-left: 6px; }
</style>
</head>
<body>

  <section class="card card--front">
    <div class="brand">
      <div class="brand-dot"></div>
      <div class="brand-name">Broken Spur Rigs</div>
      <div class="brand-rule"></div>
    </div>
    <div class="divider"></div>
    <div class="contact">
      <div class="contact-name">Dale Porvick</div>
      <div class="contact-title">Owner</div>
      <div class="contact-address">
        48310 E Calloway Ridge Rd S<br>
        STE 217<br>
        Marsh Hollow, CO 80219
      </div>
      <div class="contact-line">
        <svg viewBox="0 0 24 24" aria-hidden="true"><path d="M6.6 10.8a15 15 0 0 0 6.6 6.6l2.2-2.2c.3-.3.7-.4 1-.2 1.1.4 2.3.6 3.6.6.6 0 1 .4 1 1V20c0 .6-.4 1-1 1A17 17 0 0 1 3 4c0-.6.4-1 1-1h3.5c.6 0 1 .4 1 1 0 1.3.2 2.5.6 3.6.1.3 0 .7-.2 1z"/></svg>
        720-555-0184
      </div>
      <div class="contact-line">
        <svg viewBox="0 0 24 24" aria-hidden="true"><path d="M2 5h20v14H2z M2 5l10 8 10-8" /></svg>
        dale@brokenspurrigs.example
      </div>
      <div class="contact-line">
        <svg viewBox="0 0 24 24" aria-hidden="true"><circle cx="12" cy="12" r="10"/></svg>
        www.brokenspurrgis.example
      </div>
    </div>
  </section>

  <section class="card card--back">
    <div class="brand">
      <div class="brand-dot"></div>
      <div class="brand-name">Broken Spur Rigs</div>
      <div class="brand-rule"></div>
    </div>
    <div class="social">
      <span class="social-dot"></span>
      <span class="social-dot"></span>
      <span class="social-dot"></span>
      <span class="social-dot"></span>
      <span class="social-handle">@brokenspurrigs</span>
    </div>
  </section>

</body>
</html>
```